Family Farm Looking for meat label

We have a small farm in Italy with two types of cow "Piemontese" and "Pezzata Rossa Valdostana". We need label ( about 5x5 cm) to put on the boxes and on every single piece of meat.

Target Market(s)

private client

Industry/Entity Type

family farm

Colors

Designer to choose colors to be used in the design.

Requirements
Must have
• to write "Azienda Agricola Il Roveto" and the cow like our cow not differently. the Piemontese breed cow has the typical physical shapes as in the photo. No photo on the label just a drawing o something like that.
Nice to have
• just a one label, clear, fine and clean . Maybe with pastel color or watercolor. We are a small family farm.
Should not have
• no photo, no another type of cow

```html
<!DOCTYPE html>
<html lang="en">
<head>
<meta charset="utf-8">
<title>Il Roveto – Beef Label</title>
<link href="https://fonts.googleapis.com/css2?family=Bebas+Neue&family=Archivo+Black&family=Montserrat:wght@600&display=swap" rel="stylesheet">
<style>
  :root {
    --backdrop: #acadac;
    --label-green: #32b454;
    --illustration-tone: #2a9a46;
    --ink: #111111;
    --paper: #ffffff;
  }
  * { margin: 0; padding: 0; box-sizing: border-box; }
  html, body { width: 1200px; height: 1200px; overflow: hidden; }
  body { background: var(--backdrop); position: relative; }

  .label {
    position: absolute;
    left: 296px; top: 296px;
    width: 607px; height: 607px;
    background: var(--label-green);
    border-radius: 28px;
    color: var(--paper);
    font-family: "Bebas Neue", sans-serif;
  }
  .brand-name {
    position: absolute;
    left: 0; right: 0; top: 58px;
    text-align: center;
    font-size: 56px;
    line-height: 1;
    letter-spacing: 1px;
  }
  .brand-tagline {
    position: absolute;
    left: 0; right: 0; top: 144px;
    text-align: center;
    font-family: "Montserrat", sans-serif;
    font-weight: 600;
    font-size: 17px;
    letter-spacing: 6.2px;
    color: var(--ink);
    padding-left: 6px;
  }
  .breed {
    position: absolute;
    top: 208px;
    font-size: 66px;
    line-height: 62px;
    letter-spacing: -0.5px;
  }
  .breed--piemontese { left: 24px; }
  .breed--valdostana { right: 22px; text-align: right; }

  .cattle-illustration {
    position: absolute;
    top: 336px;
    height: 149px;
    background: var(--illustration-tone);
    border-radius: 6px;
  }
  .cattle-illustration--piemontese { left: 64px; width: 246px; }
  .cattle-illustration--valdostana { left: 314px; width: 230px; }

  .claims {
    position: absolute;
    left: 0; right: 0; top: 486px; height: 92px;
  }
  .claim-group {
    position: absolute;
    text-align: center;
    font-size: 21px;
    line-height: 22px;
  }
  .claim-group--left { left: 22px; width 140px; width: 140px; top: 0; }
  .claim-group--left p + p { margin-top: 10px; }
  .claim-group--right { left: 437px; width: 140px; top: 4px; }
  .divider {
    position: absolute;
    top: 0; width: 2px; height: 86px;
    background: var(--ink);
  }
  .divider--left { left: 165px; }
  .divider--right { left: 440px; }
  .claim-main {
    position: absolute;
    left: 167px; width: 273px; top: 26px;
    text-align: center;
    font-family: "Archivo Black", sans-serif;
    font-size: 31px;
    letter-spacing: 1px;
  }
  .net-weight {
    color: var(--ink);
    font-size: 27px;
    margin-top: 8px;
  }
</style>
</head>
<body>
  <main class="label">
    <div class="brand-name">IL ROVETO</div>
    <div class="brand-tagline">AZIENDA AGRICOLA IL ROVETO</div>

    <h1 class="breed breed--piemontese">PIEMONTESE<br>COW BEEF</h1>
    <h1 class="breed breed--valdostana">PEZZATA ROSSA<br>VALDOSTANA BEEF</h1>

    <div class="cattle-illustration cattle-illustration--piemontese" role="img" aria-label="Engraved drawing of a muscular Piemontese bull standing in profile"></div>
    <div class="cattle-illustration cattle-illustration--valdostana" role="img" aria-label="Engraved drawing of a Pezzata Rossa Valdostana cow standing, facing the viewer"></div>

    <section class="claims">
      <div class="claim-group claim-group--left">
        <p>NO ADDED<br>HORMONES</p>
        <p>NO ANIMAL BY<br>PRODUCTS</p>
      </div>
      <span class="divider divider--left"></span>
      <div class="claim-main">GRASS FED</div>
      <span class="divider divider--right"></span>
      <div class="claim-group claim-group--right">
        <p>ANTIBIOTIC<br>FREE</p>
        <p class="net-weight">250G</p>
      </div>
    </section>
  </main>
</body>
</html>
```